Corvane Partners Web Design

Dear all
I need a web design for a financial services site. We are a broker who deals with many different financial institutions and require a clean, simple and instantly impressive site based on the colour scheme that SketchGuild created for us. A landing page (www.crvnp.mx) gives an idea of the logo and clour scheme but we are looking at either a one page site with rollover text boxes or a 3 or 4 page site depending on the preference of the designer and the best user experience. The site“s purpose is to give confidence that the company exists rather than impart pages of information although we would like this to be a site that can expand over time as the company grows. For now the requirement is for a clear set of possibly changing images at the centre of a white screen that relate to finance in general nad the benefits of wealth creation as well as sectios either along the top or bottom - Our Company, Our Approach, Our services, Our clients, Contact (user to fill in contact box to be sent to info@crvnp.mx. The text for each of these boxes I assume can be added by the coding team here, it the overall look and feel that I am looking for from SketchGuild - deadline can be extended if necessary but I was hoping to wrap this all up in October

Target Market(s)

Succesful individuals looking to maximise returns on their investment via world class financial institutions and supported throughout by qualified independent financial advisors

Industry/Entity Type

Finance

Requirements
Must have
• Logo and color scheme of the logo design SketchGuild sent - I have all these sourcefiles, pantone and fonts

```html
<!DOCTYPE html>
<html lang="en">
<head>
<meta charset="utf-8">
<title>Corvane Partners – Wealth Management</title>
<link href="https://fonts.googleapis.com/css2?family=Quicksand:wght@400;500&family=Arimo:wght@400;700&display=swap" rel="stylesheet">
<style>
  :root {
    --navy: #1e3a66;
    --orange: #f0a037;
    --slate: #868b8f;
    --paper: #f2f2f2;
    --white: #ffffff;
    --text: #3a3a3a;
    --rule: #cfd2d5;
  }
  * { box-sizing: border-box; margin: 0; padding: 0; }
  html, body { width: 1200px; height: 1071px; overflow: hidden; background: var(--white); }
  body { position: relative; font-family: "Arimo", Arial, sans-serif; color: var(--text); }

  .top-band { position: absolute; left: 0; top: 0; width: 1200px; height: 47px; background: var(--paper); }
  .logo-arch { position: absolute; left: 490px; top: 10px; width: 220px; height: 180px; border-radius: 50%; background: var(--white); }
  .brand { position: absolute; left: 0; top: 0; width: 1200px; text-align: center; }
  .brand-mark { position: absolute; left: 578px; top: 40px; width: 44px; height: 44px; border-radius: 50%; background: var(--navy); }
  .brand-name { position: absolute; left: 0; top: 126px; width: 1200px; font-family: "Quicksand", sans-serif; font-weight: 400; font-size: 26px; letter-spacing: 10px; color: var(--navy); }
  .brand-tagline { position: absolute; left: 0; top: 183px; width: 1200px; font-family: "Quicksand", sans-serif; font-size: 17px; letter-spacing: 2px; color: var(--navy); }

  .main-nav { position: absolute; left: 0; top: 228px; width: 1200px; height: 26px; background: var(--navy); }
  .main-nav a { position: absolute; top: 0; height: 26px; line-height: 26px; text-align: center; color: var(--white); font-size: 12.3px; text-decoration: none; border-right: 1px solid #17304f; }
  .main-nav a.active { background: var(--orange); }

  .intro-title { position: absolute; left: 170px; top: 294px; font-family: "Quicksand", sans-serif; font-weight: 400; font-size: 25px; letter-spacing: 1px; color: var(--navy); }
  .intro-rule { position: absolute; left: 170px; top: 332px; width: 343px; height: 1px; background: var(--rule); }
  .intro-text { position: absolute; left: 170px; width: 333px; font-size: 11px; line-height: 13.8px; color: var(--text); }

  .btn { position: absolute; height: 26px; line-height: 26px; text-align: center; background: var(--navy); color: var(--white); font-size: 11.5px; border-radius: 3px; text-decoration: none; }

  .hero-frame { position: absolute; left: 543px; top: 299px; width: 487px; height: 250px; background: var(--white); box-shadow: 0 1px 6px rgba(0,0,0,.3); border-radius: 2px; }
  .hero-photo { position: absolute; left: 5px; top: 6px; width: 477px; height: 239px; background: linear-gradient(135deg, #2b3d58 0%, #8ea5c4 35%, #d6e0ec 55%, #9fb3cd 80%, #6d86a8 100%); }
  .hero-caption { position: absolute; left: 5px; top: 176px; width: 271px; height: 53px; background: rgba(120,124,130,.88); border-radius: 0 3px 3px 0; padding: 3px 10px; font-family: "Quicksand", sans-serif; font-size: 19px; line-height: 21px; letter-spacing: 1px; color: var(--white); }

  .section-rule { position: absolute; left: 170px; top: 582px; width: 860px; height: 1px; background: linear-gradient(90deg, transparent, #c6c9cc 15%, #c6c9cc 85%, transparent); }

  .feature-card { position: absolute; top: 618px; width: 187px; height: 236px; border: 1px solid #d9dbdd; border-radius: 3px; background: linear-gradient(#ffffff, #f3f3f3); text-align: center; }
  .feature-card h2 { margin-top: 10px; font-family: "Quicksand", sans-serif; font-weight: 500; font-size: 19px; letter-spacing: 1px; color: var(--navy); }
  .feature-icon { width: 66px; height: 66px; margin: 12px auto 0; background: var(--orange); }
  .feature-card p { margin: 15px 12px 0; font-size: 11px; line-height: 13.8px; color: var(--text); }
  .feature-card .btn { left: 49px; bottom: 16px; width: 88px; }

  .footer-nav { position: absolute; left: 0; top: 889px; width: 1200px; height: 28px; background: var(--slate); text-align: center; font-size: 11px; line-height: 28px; color: var(--white); }
  .footer-nav a { color: var(--white); text-decoration: none; }
  .footer-nav .sep { margin: 0 15px; color: #c9ccce; }

  .contact { position: absolute; left: 0; top: 917px; width: 1200px; height: 154px; background: var(--paper); text-align: center; }
  .contact h3 { position: absolute; left: 0; top: 18px; width: 1200px; font-size: 17.5px; font-weight: 700; color: var(--navy); }
  .contact-rule { position: absolute; left: 425px; width: 350px; height: 1px; background: linear-gradient(90deg, transparent, #d3d5d7, transparent); }
  .contact-line { position: absolute; left: 0; top: 57px; width: 1200px; font-size: 11.5px; color: var(--navy); }
  .contact-line b { font-weight: 700; }
  .contact-line .sep { margin: 0 14px; color: #666; }
  .social { position: absolute; top: 82px; width: 19px; height: 19px; border-radius: 3px; background: #4a6fa5; }
  .copyright { position: absolute; left: 0; top: 128px; width: 1200px; font-size: 10.5px; color: #777; }
  .copyright b { color: #666; }
</style>
</head>
<body>

<header>
  <div class="top-band"></div>
  <div class="logo-arch"></div>
  <div class="brand">
    <span class="brand-mark"></span>
    <div class="brand-name">CORVANE PARTNERS</div>
    <div class="brand-tagline">WEALTH MANAGEMENT</div>
  </div>
  <nav class="main-nav">
    <a class="active" href="#" style="left:170px;width:101px;">HOME</a>
    <a href="#" style="left:271px;width:157px;">OUR COMPANY</a>
    <a href="#" style="left:428px;width:161px;">OUR APPROACH</a>
    <a href="#" style="left:589px;width:158px;">OUR SERVICES</a>
    <a href="#" style="left:747px;width:143px;">OUR CLIENTS</a>
    <a href="#" style="left:890px;width:147px;border-right:none;">CONTACT US</a>
  </nav>
</header>

<main>
  <h1 class="intro-title">Welcome to Our Site</h1>
  <div class="intro-rule"></div>
  <p class="intro-text" style="top:350px;">Lorem ipsum dolor sit amet, consectetur adipisicing elit, sed do eiusmod tempor incididunt ut labore et dolore magna aliqua. Ut enimad minim veniam, quis nostrud exercitation ullamco laboris nisiut aliquip ex ea commodo consequat. Duis aute irure dolor in reprehenderit in voluptate velit esse cillum dolore eu fugiat nulla pariatur.</p>
  <p class="intro-text" style="top:447px;">Lorem ipsum dolor sit amet, consectetur adipisicing elit, sed do eiusmod tempor incididunt ut labore et dolore magna aliqua. Ut enimad minim veniam, quis nostrud exercitation ullamco laboris nisiut aliquip ex ea commodo consequat.</p>
  <a class="btn" href="#" style="left:170px;top:524px;width:88px;">Read More</a>

  <div class="hero-frame">
    <div class="hero-photo" role="img" aria-label="Photo of a calculator, a stack of coins and a financial chart printout in blue tones"></div>
    <div class="hero-caption">Offering The Most<br>Compatitive Rates &amp; Fees</div>
  </div>

  <div class="section-rule"></div>

  <section class="feature-card" style="left:170px;">
    <h2>Our Company</h2>
    <div class="feature-icon" role="img" aria-label="Icon of a rising arrow over bar chart"></div>
    <p>Lorem ipsum dolor sit amet, consectetur adipisicing elit, sed do eiusmod tempor incididunt ut labore et dolore....</p>
    <a class="btn" href="#">Read More</a>
  </section>
  <section class="feature-card" style="left:394px;">
    <h2>Our Approach</h2>
    <div class="feature-icon" role="img" aria-label="Icon of a person working at a desk"></div>
    <p>Lorem ipsum dolor sit amet, consectetur adipisicing elit, sed do eiusmod tempor incididunt ut labore et dolore....</p>
    <a class="btn" href="#">Read More</a>
  </section>
  <section class="feature-card" style="left:619px;">
    <h2>Our Services</h2>
    <div class="feature-icon" role="img" aria-label="Icon of a person running on gears"></div>
    <p>Lorem ipsum dolor sit amet, consectetur adipisicing elit, sed do eiusmod tempor incididunt ut labore et dolore....</p>
    <a class="btn" href="#">Read More</a>
  </section>
  <section class="feature-card" style="left:844px;">
    <h2>Our Clients</h2>
    <div class="feature-icon" role="img" aria-label="Icon of two people shaking hands"></div>
    <p>Lorem ipsum dolor sit amet, consectetur adipisicing elit, sed do eiusmod tempor incididunt ut labore et dolore....</p>
    <a class="btn" href="#">Read More</a>
  </section>
</main>

<footer>
  <nav class="footer-nav">
    <a href="#">Home</a><span class="sep">|</span><a href="#">Our Company</a><span class="sep">|</span><a href="#">Our Approach</a><span class="sep">|</span><a href="#">Our services</a><span class="sep">|</span><a href="#">Our clients</a><span class="sep">|</span><a href="#">Contact us</a>
  </nav>
  <div class="contact">
    <h3>Get In Touch</h3>
    <div class="contact-rule" style="top:43px;"></div>
    <div class="contact-line"><b>Tel :</b> +52 (55) 4107 2293<span class="sep">|</span><b>Email :</b> info@crvnp.mx</div>
    <span class="social" style="left:563px;"></span>
    <span class="social" style="left:593px;background:#5aa9dc;"></span>
    <span class="social" style="left:623px;background:#2b7bb4;"></span>
    <div class="contact-rule" style="top:113px;"></div>
    <div class="copyright">Copyright © <b>Corvane Partners</b> 2013.All Right Reserved.</div>
  </div>
</footer>

</body>
</html>
```